Redesign our company's business card. RVL BUSINESS CARD 2015

We are an Audio Visual Production company with a flare of marketing and sales. Lights camera ACTION!! We are Production and creative designers and thinkers whom provide first class service for many fortune 500 companies that Exhibit at trade shows and sales meetings.

Double sided, sleek, fashionable, and modern.

www.brightlanemedia.example

Think QRV'S Sidelines

Target Market(s)

Trade Show Mangers, Event coordinators, Project managers,

Industry/Entity Type

Marketing

Contact Information for Business Card

Name Tile, Logo, Slogan, photos of our work on the back. Facebook and twitter

Font styles to use
Sans Serif
Decorative
Script

Colors
33a6d7
ffffff
0692cd
cee9f5

Requirements
Must have
• Multi color, professional, Upscale,
• CREATING GREAT PARTNERSHIPS THAT PRODUCE AMAZING RESULTS
Nice to have
• Photos of our work on the back
Should not have
• Address or fax.

```html
<!DOCTYPE html>
<html lang="en">
<head>
<meta charset="utf-8">
<title>RVL Business Card</title>
<link rel="stylesheet" href="https://fonts.googleapis.com/css2?family=Exo+2:wght@400;500;600&display=swap">
<style>
  :root {
    --page: #e9ecef;
    --card-white: #ffffff;
    --card-shade: #eef0f2;
    --blue-deep: #0692cd;
    --blue-mid: #33a6d7;
    --blue-pale: #cee9f5;
    --silver-light: #f4f5f6;
    --silver-dark: #9da3a8;
    --ink-grey: #8a9096;
    --text-white: #ffffff;
  }
  * { margin: 0; padding: 0; box-sizing: border-box; }
  html, body { width: 1200px; height: 803px; overflow: hidden; }
  body {
    background: var(--page);
    font-family: "Exo 2", sans-serif;
    position: relative;
  }
  .card {
    position: absolute;
    top: 247px;
    width: 540px;
    height: 309px;
    background: linear-gradient(135deg, var(--card-white) 40%, var(--card-shade));
    box-shadow: 0 6px 18px rgba(0,0,0,0.18);
    overflow: hidden;
  }
  .card--front { left: 40px; }
  .card--back { left: 620px; }
  .card-art { position: absolute; inset: 0; width: 100%; height: 100%; }

  .brand {
    position: absolute;
    display: flex;
    align-items: center;
    gap: 14px;
  }
  .brand-dot {
    border-radius: 50%;
    background: var(--blue-mid);
    flex: none;
  }
  .brand-words { display: flex; flex-direction: column; }
  .brand-name, .brand-full {
    color: var(--ink-grey);
    font-weight: 500;
    letter-spacing: 0.06em;
    text-transform: uppercase;
    line-height: 1;
  }
  .card--front .brand { left: 120px; top: 112px; }
  .card--front .brand-dot { width: 70px; height: 70px; }
  .card--front .brand-name { font-size: 52px; }
  .card--front .brand-full { font-size: 12px; margin-top: 8px; padding-top: 5px; border-top: 1px solid var(--ink-grey); }

  .slogan {
    position: absolute;
    left: 40px;
    width: 430px;
    top: 232px;
    text-align: center;
    font-size: 9px;
    font-weight: 500;
    letter-spacing: 0.1em;
    color: var(--blue-deep);
    text-transform: uppercase;
  }

  .card--back .brand { left: 40px; top: 124px; gap: 10px; }
  .card--back .brand-dot { width: 46px; height: 46px; }
  .card--back .brand-name { font-size: 34px; }
  .card--back .brand-full { font-size: 8px; margin-top: 5px; padding-top: 4px; border-top: 1px solid var(--ink-grey); }

  .site-vertical {
    position: absolute;
    right: 14px;
    top: 22px;
    writing-mode: vertical-rl;
    font-size: 10px;
    letter-spacing: 0.08em;
    color: #4b5055;
  }

  .contact-panel {
    position: absolute;
    left: 318px;
    top: 62px;
    color: var(--text-white);
  }
  .person-name { font-size: 24px; font-weight: 500; letter-spacing: 0.06em; text-transform: uppercase; line-height: 1; }
  .person-role { font-size: 9px; letter-spacing: 0.1em; text-transform: uppercase; margin-top: 8px; }
  .contact-list { list-style: none; margin-top: 30px; }
  .contact-item { display: flex; align-items: center; gap: 8px; font-size: 10px; margin-bottom: 10px; line-height: 1.2; white-space: nowrap; }
  .contact-icon { width: 16px; height: 16px; flex: none; }
</style>
</head>
<body>

<section class="card card--front" aria-label="Card front">
  <svg class="card-art" viewBox="0 0 540 309" aria-hidden="true">
    <defs>
      <linearGradient id="silver-front" x1="0" x2="1">
        <stop offset="0" stop-color="var(--silver-dark)"/>
        <stop offset="0.45" stop-color="var(--silver-light)"/>
        <stop offset="1" stop-color="var(--silver-dark)"/>
      </linearGradient>
    </defs>
    <path d="M506 0 H540 V309 H492 V40 Q492 8 506 0 Z" fill="url(#silver-front)"/>
  </svg>
  <div class="brand">
    <span class="brand-dot"></span>
    <div class="brand-words">
      <span class="brand-name">RVL</span>
      <span class="brand-full">Riverlane Visual Labs</span>
    </div>
  </div>
  <p class="slogan">Creating great partnerships that produce amazing results</p>
  <span class="site-vertical">www.brightlanemedia.example</span>
</section>

<section class="card card--back" aria-label="Card back">
  <svg class="card-art" viewBox="0 0 540 309" aria-hidden="true">
    <defs>
      <radialGradient id="blue-glow" cx="0.45" cy="0.3" r="0.8">
        <stop offset="0" stop-color="#3fd0f2"/>
        <stop offset="0.5" stop-color="var(--blue-mid)"/>
        <stop offset="1" stop-color="var(--blue-deep)"/>
      </radialGradient>
      <linearGradient id="silver-back" x1="0" x2="1">
        <stop offset="0" stop-color="var(--silver-dark)"/>
        <stop offset="0.5" stop-color="var(--silver-light)"/>
        <stop offset="1" stop-color="var(--silver-dark)"/>
      </linearGradient>
    </defs>
    <path d="M300 0 H512 V309 H336 L278 60 Q268 10 300 0 Z" fill="url(#blue-glow)"/>
    <path d="M508 0 H540 V309 H516 V44 Q516 10 508 0 Z" fill="url(#silver-back)"/>
    <rect x="298" y="66" width="8" height="26" fill="url(#silver-back)"/>
  </svg>
  <div class="brand">
    <span class="brand-dot"></span>
    <div class="brand-words">
      <span class="brand-name">RVL</span>
      <span class="brand-full">Riverlane Visual Labs</span>
    </div>
  </div>
  <div class="contact-panel">
    <h1 class="person-name">Dana Reyes</h1>
    <p class="person-role">General Manager</p>
    <ul class="contact-list">
      <li class="contact-item">
        <svg class="contact-icon" viewBox="0 0 16 16"><circle cx="8" cy="8" r="7" fill="none" stroke="#fff"/><path d="M5.5 4.5 L7 6 L6.2 7 Q7 9 9 9.8 L10 9 L11.5 10.5 L10.5 11.5 Q6 11 4.5 5.5 Z" fill="#fff"/></svg>
        555 010 4477
      </li>
      <li class="contact-item">
        <svg class="contact-icon" viewBox="0 0 16 16"><circle cx="8" cy="8" r="7" fill="none" stroke="#fff"/><rect x="5.8" y="4" width="4.4" height="8" rx="0.8" fill="none" stroke="#fff"/></svg>
        555 010 4478
      </li>
      <li class="contact-item">
        <svg class="contact-icon" viewBox="0 0 16 16"><circle cx="8" cy="8" r="7" fill="none" stroke="#fff"/><rect x="4.5" y="5.5" width="7" height="5" fill="#fff"/><path d="M4.5 5.5 L8 8.5 L11.5 5.5" fill="none" stroke="var(--blue-mid)" stroke-width="0.8"/></svg>
        hello@brightlanemedia.example
      </li>
      <li class="contact-item">
        <svg class="contact-icon" viewBox="0 0 16 16"><circle cx="8" cy="8" r="7" fill="none" stroke="#fff"/><circle cx="8" cy="8" r="3.8" fill="none" stroke="#fff" stroke-width="0.8"/><path d="M4.2 8 H11.8 M8 4.2 V11.8" stroke="#fff" stroke-width="0.8"/></svg>
        www.brightlanemedia.example
      </li>
    </ul>
  </div>
</section>

</body>
</html>
```